Logo for Internal Medicine practice

I want a logo for my Internal Medicine practice, I would like it to be with my name on it which is Lorena Benítez Prado.

I would like the business card to say the following (it is in Spanish since my practice is in Spanish):

Lorena Benítez Prado
Medicina Interna
Cel. 5587316420
lorenabenitezprado@correovela.com

Logo Text

Lorena Benítez

```html
<!DOCTYPE html>
<html lang="es">
<head>
<meta charset="utf-8">
<title>Lorena Benítez — Medicina Interna</title>
<link href="https://fonts.googleapis.com/css2?family=Poppins:wght@300;400;600&display=swap" rel="stylesheet">
<style>
  :root {
    --page-bg: #e6e6e6;
    --card-white: #ffffff;
    --teal: #1cc7b3;
    --blue: #1f78d1;
    --grad-start: #00c9bb;
    --grad-end: #0077d0;
    --text-grey: #555b60;
    --logo-light: #ffffff;
  }
  * { box-sizing: border-box; margin: 0; padding: 0; }
  html, body {
    width: 1200px; height: 802px; overflow: hidden;
    background: var(--page-bg);
    font-family: "Poppins", sans-serif;
  }
  .stage {
    position: relative; width: 1200px; height: 802px;
    display: flex; align-items: center; justify-content: center; gap: 50px;
  }
  .card {
    position: relative; width: 520px; height: 297px;
    box-shadow: 0 6px 18px rgba(0,0,0,0.12);
    overflow: hidden;
  }
  .card--front { background: var(--card-white); }
  .card--back {
    background: linear-gradient(100deg, var(--grad-start) 0%, #00a6c9 50%, var(--grad-end) 100%);
  }
  .brand {
    position: absolute; left: 0; right: 0; text-align: center;
    font-weight: 300; white-space: nowrap; letter-spacing: 0.5px;
  }
  .card--front .brand {
    top: 66px; padding-left: 80px; font-size: 36px; color: var(--teal);
  }
  .card--back .brand {
    top: 120px; font-size: 44px; color: var(--logo-light);
  }
  .person {
    position: absolute; left: 70px; top: 164px;
  }
  .person__name {
    font-weight: 600; font-size: 20px; color: var(--teal);
    text-transform: uppercase; letter-spacing: 0.3px; line-height: 1.1;
  }
  .person__role {
    font-size: 13px; color: var(--blue); line-height: 1.5;
  }
  .divider {
    position: absolute; left: 70px; right: 24px; top: 218px;
    height: 1px; background: var(--teal);
  }
  .contact {
    position: absolute; left: 70px; top: 228px;
    list-style: none; font-size: 12px; color: var(--text-grey);
  }
  .contact__item { display: flex; align-items: center; gap: 8px; line-height: 20px; }
  .contact__item--phone { font-size: 15px; }
  .contact__icon { width: 12px; height: 12px; flex: none; }
</style>
</head>
<body>
<main class="stage">
  <section class="card card--front" aria-label="Tarjeta, frente">
    <div class="brand">Lorena Benítez</div>
    <div class="person">
      <p class="person__name">Lorena Benítez Prado</p>
      <p class="person__role">Medicina Interna</p>
    </div>
    <div class="divider"></div>
    <ul class="contact">
      <li class="contact__item contact__item--phone">
        <svg class="contact__icon" viewBox="0 0 12 12"><rect x="3" y="0.8" width="6" height="10.4" rx="1.2" fill="none" stroke="#1f78d1" stroke-width="1.4"/><circle cx="6" cy="9.2" r="0.7" fill="#1f78d1"/></svg>
        5587316420
      </li>
      <li class="contact__item">
        <svg class="contact__icon" viewBox="0 0 12 12"><rect x="0.5" y="2" width="11" height="8" rx="1" fill="#1f78d1"/><path d="M1 2.5 L6 6.5 L11 2.5" fill="none" stroke="#ffffff" stroke-width="1"/></svg>
        lorenabenitezprado@correovela.com
      </li>
    </ul>
  </section>

  <section class="card card--back" aria-label="Tarjeta, reverso">
    <div class="brand">Lorena Benítez</div>
  </section>
</main>
</body>
</html>
```